Systems and Technology Consultants - Website

Design & Build a website for a new company which operates in the Systems and Technology space for Transportation, Government and Commercial sectors.

Overall design should be minimalist in nature.
Should also have a feed that provides news and event updates on the main page.
Logo has already been awarded and should be incorporated into the site.

We like the overall layout, functionality and simplicity of the below sites. Submitted designs could be similar to or a combination of the aspects on these sites, or perhaps a whole different concept - we are open to new ideas.
Vortrane.com
Merp.it

Update 1 Dated 27 May 2014

All I am moving away from the Merp.it website and would like it to be more aligned with Vortrane.com not only in layout but in functionality. I will be extending the deadline of this design brief for two weeks to incorporate additional requirements and will add addtional funding to the project.

Apologies for not having more information available to provide but with so many submissions its getting confusing.

Thanks Dermot
Updates

Please note that the brief has been updated and the deadline has been extended.

Important: We will need two language versions of the website, English and Arabic; the website is hosted on HostPeak

Hello All, Thank you for your submissions. We have narrowed it down to the final 6 designers and I just wanted to take a moment and provide a bit of feedback regarding the concepts that we like and the modifications we are looking for. First, let me mention some of the design functions we like. - At the top of the homepage we really like the "region" or "language" tab so that the website can be viewed in both English and Arabic. - We like the homepage to have clear color variation so that the different sections of the homepage are distinct. Additionally, we like the bottom portion of the homepage to be in red. We feel that draws attention to our contact information. Again, we would like the colors to integrate black, gray-scale, red, etc. - Having a search tab at the top of the home page, or integrated into the main image, so that the site is easy to navigate. - We especially like the main image to have the scrolling tabs at the bottom so it is easy to browse the services offered (Consultancy, Solutions Architecture, Masters Systems Integration, Independent Design Review). - In regards to the services offered tab we really like the idea that a few people presented that have the outside of our logo with an icon in the middle of consultancy, solutions, etc., etc. Secondly, as mentioned in our brief we really enjoy the design of vortrane site. Specially, we enjoy the strong iconic images they use, the way the tabs at the top scroll easily, and contact us page that generates an email. Lastly, I've included some photos of the concept we have been working on. What we are trying to demonstrate is how our company offers a range of services that are essentially linked together. We provide individual services that when combined present the full service package. We would like this concept to be integrated into the over concept of our website. Please feel free to ask for clarification of any of the above points or contact us if you have any additional questions. We appreciate all of your hard work and are very excited to see the updated designs. Best, Miriam Dowbrook Plenvaro Senior Program Manager miriam.dowbrook@plenvaro-mail.com

Industry/Entity Type

Government

Font styles to use
Serif
Sans Serif

Requirements
Must have
• Must work on/adapt to various/mobile devices (responsive)
Must be simple and straightforward
Colors should be in line/matching with logo
2 language versions: English and Arabic (no Thai)
Services should be the first group/row of items after/below the main image
Note: the website will be hosted by hostpeak
Nice to have
• Submit feedback form
What's New section
The banner at the bottom of the site should not be too large; we would like a narrow one more
It would be nice if the header/top banner (with Home, About, etc. tabs) could stay in place as you scroll down (like Vortrane and Chatterly)
We will likely only use one image with a Company slogan on the Home page rather than a carousel of images to rotate through
Should not have
• This is the existing website: http://www.plenvaro-example.org
We do not like the animation, the way the banner icons/titles bounce
Not simple enough, we don't like the functionality or how pages load so slowly
We do not like the logo centered - it should be at the left
The banner and its tabs should not be towards the right, we would like them to be centered, to go all the way across and to be below the logo

```html
<!DOCTYPE html>
<html lang="en">
<head>
<meta charset="utf-8">
<title>Plenvaro International</title>
<link href="https://fonts.googleapis.com/css2?family=Montserrat+Alternates:wght@500;600;700&family=Questrial&family=Roboto:wght@300;400&display=swap" rel="stylesheet">
<style>
:root{
  --red:#e82027;
  --red-dark:#a3161c;
  --grey-band:#ededed;
  --text:#555;
  --muted:#888;
  --white:#fff;
  --line:#cfcfcf;
}
*{margin:0;padding:0;box-sizing:border-box}
html,body{width:1200px;height:1200px;overflow:hidden;background:var(--white)}
body{position:relative;font-family:'Questrial',sans-serif;color:var(--text)}
.abs{position:absolute}
.display{font-family:'Montserrat Alternates',sans-serif}

/* top navigation */
.topnav{top:0;left:0;width:1200px;height:47px;background:var(--white);border-bottom:2px solid var(--red)}
.nav-home{left:175px;top:0;width:123px;height:47px;background:var(--white);box-shadow:0 0 6px rgba(0,0,0,.15);display:flex;align-items:center;justify-content:center;gap:7px;color:var(--red);font-size:13px;font-weight:600}
.nav-home .mark{width:10px;height:10px;background:var(--red)}
.nav-item{top:18px;font-size:12.5px;color:#aaa;font-weight:500;letter-spacing:.3px}
.social{top:16px;width:16px;height:16px;border-radius:50%;background:#d8d8d8}
.social.active{background:var(--red)}

/* hero */
.hero{left:0;top:47px;width:1200px;height:371px;background:linear-gradient(100deg,#e8242a 0%,#e02128 50%,#b8161c 72%,#7a0f12 100%)}
.brand-block{left:0;top:118px;width:1200px;text-align:center;color:var(--white)}
.brand-sq{width:46px;height:46px;border:9px solid var(--white);margin:0 auto 16px;transform:rotate(45deg)}
.brand-name{font-family:'Montserrat Alternates',sans-serif;font-weight:700;font-size:34px;letter-spacing:12px}
.brand-sub{font-family:'Montserrat Alternates',sans-serif;font-weight:700;font-size:13px;letter-spacing:6px;margin-top:2px}
.hero-slogan{left:0;top:294px;width:1200px;text-align:center;color:var(--white);font-family:'Montserrat Alternates',sans-serif;font-weight:600;font-size:17px;line-height:18px}

/* welcome */
.welcome{left:0;top:418px;width:1200px;height:214px;background:var(--grey-band)}
.welcome h1{position:absolute;top:32px;width:1200px;text-align:center;color:var(--red);font-family:'Montserrat Alternates',sans-serif;font-weight:600;font-size:21px;letter-spacing:1px}
.welcome p{position:absolute;top:69px;left:200px;width:800px;text-align:center;font-family:'Roboto',sans-serif;font-weight:300;font-size:18.5px;line-height:22.5px;color:#666}

/* feeds */
.feed-title{top:657px;color:var(--red);font-family:'Montserrat Alternates',sans-serif;font-weight:600;font-size:16.5px;letter-spacing:.5px}
.feed-rule{top:682px;height:1px;background:var(--line)}
.news-img{left:194px;top:693px;width:148px;height:125px;background:linear-gradient(135deg,#e6e8ea,#a9afb4);border:1px solid #bbb}
.item-title{top:707px;color:var(--red);font-size:13px}
.item-text{font-size:10px;line-height:12.5px;color:#777}
.item-link{font-size:10px;color:var(--red)}
.event-date{left:941px;top:712px;font-size:10.5px;color:var(--red);letter-spacing:1px}

/* services */
.services{left:0;top:863px;width:1200px;height:233px;background:var(--red)}
.services h2{position:absolute;top:32px;width:1200px;text-align:center;color:var(--white);font-family:'Montserrat Alternates',sans-serif;font-weight:600;font-size:20px;letter-spacing:1px}
.svc{top:83px;width:143px;height:150px;display:flex;flex-direction:column;align-items:center;justify-content:center;gap:12px;color:var(--white);font-family:'Montserrat Alternates',sans-serif;font-weight:600;font-size:11.5px;letter-spacing:.6px}
.svc.active{background:var(--red-dark);font-size:13px}
.svc svg{width:38px;height:38px;fill:var(--white)}

/* footer */
.footer{left:0;top:1096px;width:1200px;height:104px;text-align:center}
.foot-brand{position:absolute;top:16px;width:1200px;color:var(--red);font-family:'Montserrat Alternates',sans-serif;font-weight:700;font-size:11px;letter-spacing:4px}
.foot-brand .sq{display:block;width:16px;height:16px;background:var(--red);margin:0 auto 6px;transform:rotate(45deg)}
.foot-line{position:absolute;width:1200px;font-size:10.5px;color:#777}
</style>
</head>
<body>

<header class="abs topnav">
  <div class="abs nav-home display"><span class="mark"></span>Home</div>
  <span class="abs nav-item display" style="left:344px">Business Unit</span>
  <span class="abs nav-item display" style="left:489px">Services &#9662;</span>
  <span class="abs nav-item display" style="left:606px">About Us</span>
  <span class="abs nav-item display" style="left:716px">Locations</span>
  <span class="abs nav-item display" style="left:825px">Contact Us</span>
  <span class="abs social active" style="left:957px"></span>
  <span class="abs social" style="left:983px"></span>
  <span class="abs social" style="left:1010px"></span>
</header>

<section class="abs hero" role="img" aria-label="Red-toned photo of a smiling engineer in a hard hat giving a thumbs up over a circuit-board pattern"></section>
<div class="abs brand-block">
  <div class="brand-sq"></div>
  <div class="brand-name">PLENVARO</div>
  <div class="brand-sub">INTERNATIONAL</div>
</div>
<p class="abs hero-slogan">Plenvaro Int. specializes in delivering quality professional services<br>and technical projects that support larger business goals.</p>

<section class="abs welcome">
  <h1>Welcome</h1>
  <p>Plenvaro specializes in delivering quality professional services and technical projects that support larger business goals.&nbsp; systems are tools that support a greater business function and need. we understand that most technical projects are conceptualized to support a larger vision with actual business goals in mind and ensure that all of our professional and certified expertise is included in our professional services to meet those goals.</p>
</section>

<h2 class="abs feed-title" style="left:194px">Latest News</h2>
<div class="abs feed-rule" style="left:194px;width:390px"></div>
<div class="abs news-img" role="img" aria-label="Photo of a businesswoman with a tablet amid floating papers against a cloudy sky"></div>
<h3 class="abs item-title" style="left:355px;font-weight:400">Lorem ipsum</h3>
<p class="abs item-text" style="left:355px;top:726px;width:235px">Lorem ipsum dolor sit amet, consectetuer adipiscing elit, sed diam nonummy nibh euismod ,<br>tincidunt ut laoreet dolore magna aliquam erat volutpat.</p>
<span class="abs item-link" style="left:355px;top:801px">Read All...</span>

<h2 class="abs feed-title" style="left:622px">Latest Events</h2>
<div class="abs feed-rule" style="left:622px;width:390px"></div>
<h3 class="abs item-title" style="left:625px;font-weight:400">Lorem ipsum</h3>
<span class="abs event-date">11-22-2014</span>
<p class="abs item-text" style="left:625px;top:729px;width:390px">Ut wisi enim ad minim veniam, quis nostrud exerci tation ullamcorper suscipit lobortis nisl ut aliquip ex ea commodo consequat.<br>Ut wisi enim ad minim veniam, quis nostrud eUt wisi enim ad minim veniam, quis nostrud exerci tation ullamcorper suscipit lobortis nisl ut aliquip ex ea commodo consequat. xerci tation ullamcorper suscipit lobortis nisl ut aliquip ex ea commodo consequat.</p>
<span class="abs item-link" style="left:625px;top:809px">Go to Event</span>

<section class="abs services">
  <h2>Our Services</h2>
  <div class="abs svc" style="left:198px">
    <svg viewBox="0 0 38 38"><circle cx="8" cy="6" r="4"/><circle cx="19" cy="6" r="4"/><circle cx="30" cy="6" r="4"/><rect x="4" y="12" width="8" height="14" rx="2"/><rect x="26" y="12" width="8" height="14" rx="2"/><rect x="14" y="16" width="10" height="4"/><rect x="17" y="20" width="4" height="14"/></svg>
    CONSULTING
  </div>
  <div class="abs svc active" style="left:364px">
    <svg viewBox="0 0 38 38"><rect x="12" y="3" width="14" height="7"/><rect x="5" y="12" width="28" height="7"/><rect x="1" y="21" width="18" height="14"/><path d="M26 22 L37 35 H15 Z"/></svg>
    ENGINEERING
  </div>
  <div class="abs svc" style="left:531px">
    <svg viewBox="0 0 38 38"><circle cx="15" cy="24" r="11"/><circle cx="15" cy="24" r="4" fill="#e82027"/><circle cx="30" cy="8" r="6"/><circle cx="30" cy="8" r="2.2" fill="#e82027"/></svg>
    MAINTENANCE
  </div>
  <div class="abs svc" style="left:697px">
    <svg viewBox="0 0 38 38"><circle cx="7" cy="6" r="4"/><rect x="3" y="11" width="8" height="24"/><path d="M10 4 H36 V28 H14 V25 H33 V7 H10 Z"/><path d="M17 33 L23 27 L29 33" stroke="#fff" stroke-width="2" fill="none"/></svg>
    OPERATIONS
  </div>
  <div class="abs svc" style="left:863px">
    <svg viewBox="0 0 38 38"><rect x="20" y="2" width="14" height="6"/><rect x="2" y="10" width="34" height="7"/><rect x="2" y="20" width="15" height="7"/><rect x="20" y="20" width="16" height="7"/><rect x="2" y="30" width="34" height="6"/></svg>
    CONSTRUCTION
  </div>
</section>

<footer class="abs footer">
  <div class="foot-brand"><span class="sq"></span>PLENVARO</div>
  <p class="foot-line" style="top:62px">Copyright 2005-2014&nbsp; www.plenvaro.biz All rights reserved.</p>
  <p class="foot-line" style="top:78px">Address: 12 larkmoor rd, eastfield, brenton 40318 &nbsp;|&nbsp; Phone numbers: +(00)-01-555-0199-0 &nbsp;&nbsp;| &nbsp;Email: info@plenvaro-mail.org</p>
</footer>

</body>
</html>
```